Mobile phone signal boosting solutions needs a website

We need a website design for the reselling of a mobile signal boosting product set. These solutions are Travik exempt and will provide an indoor signal for mobile phones. We would like to see designs that incorporate the colours and feel of our logo. The domain will be
nestorbolt.com / co.uk
Overview of the company and how it is to be used: Nestor Bolt (domain name) will work with business and end user to provide mobile signal boosting – where people struggle indoors with a mobile signal our solutions will help by finding the smallest signal and boosting it, allowing users to use voice and data over their mobile network (please note this is not wireless signal boosting)
Number of Pages:
-Home
-Solutions / How it works
-Case Studies
-Contact
Text content: Currently just use placeholders
Technical specs : Wordpress and ability to use CMS if that’s relevant
Target Market(s)
Business professional all markets /high end residential
Coding
Coded - Design and coding required
Number of Pages Required
4 page
Look and feel

```html
<!DOCTYPE html>
<html lang="en">
<head>
<meta charset="utf-8">
<title>Nestor Bolt – Mobile Signal Booster Solutions</title>
<link rel="stylesheet" href="https://fonts.googleapis.com/css2?family=Roboto:wght@400;500;700&display=swap">
<style>
:root{
  --yellow:#fcc200;
  --yellow-deep:#e3ad00;
  --ink:#111111;
  --text:#222222;
  --muted:#666666;
  --soft:#f5f5f5;
  --line:#d6d6d6;
  --white:#ffffff;
}
*{box-sizing:border-box;margin:0;padding:0}
html,body{width:1200px;height:3750px;overflow:hidden;background:var(--white)}
body{font-family:"Roboto",Arial,sans-serif;color:var(--text)}
.page{position:relative;width:1200px;height:3750px;overflow:hidden}
.abs{position:absolute}
.btn{position:absolute;display:flex;align-items:center;justify-content:center;background:var(--yellow);color:var(--ink);font-weight:500;font-size:16px;text-transform:uppercase;letter-spacing:.2px}

/* header */
.topline{left:0;top:0;width:1200px;height:6px;background:var(--yellow)}
.header{left:0;top:6px;width:1200px;height:104px;background:var(--white)}
.brand{left:150px;top:38px;display:flex;align-items:center;gap:12px}
.brand-mark{width:26px;height:26px;background:var(--yellow)}
.brand-name{font-size:30px;font-weight:500;color:var(--ink);line-height:1}
.brand-tag{left:188px;top:72px;font-size:11px;font-weight:500;color:var(--yellow);letter-spacing:.3px}
.question{left:772px;top:7px;width:279px;height:40px;background:var(--yellow);display:flex;align-items:center;justify-content:center;gap:10px;font-size:14px;color:var(--ink)}
.question b{font-weight:500}
.nav{top:74px;font-size:14.5px;font-weight:500;color:var(--ink);text-transform:uppercase}
.nav.active{color:var(--yellow)}

/* hero */
.hero-photo{left:0;top:110px;width:1200px;height:670px;background:linear-gradient(100deg,#d9d4cb 0%,#e8e6e1 35%,#cfd9df 60%,#a9b9c4 80%,#d8cfc3 100%)}
.hero-kicker{left:150px;top:243px;font-size:30px;font-weight:500;color:var(--ink)}
.hero-title{left:148px;top:288px;font-size:45px;font-weight:500;line-height:53px;color:var(--ink);text-transform:uppercase}
.hero-cut{left:0;top:690px}

/* how it works */
.section-title{position:absolute;left:0;width:1200px;text-align:center;font-weight:500;color:var(--ink);text-transform:uppercase}
.steps{left:0;top:940px}
.step-caption{position:absolute;width:170px;text-align:center;font-size:13px;line-height:16px;color:var(--muted)}

/* about */
.about{left:0;top:1361px;width:1200px;height:624px;background:var(--soft)}
.about-title{left:150px;top:1516px;font-size:33px;font-weight:500;color:var(--ink);text-transform:uppercase}
.about-sub{left:150px;top:1570px;font-size:26px;font-weight:500;line-height:22px;color:var(--yellow)}
.about-text{left:150px;top:1638px;width:410px;font-size:13.5px;line-height:22px;color:var(--muted)}
.about-ring{left:619px;top:1458px;width:440px;height:442px;border-radius:50%;border:4px solid var(--yellow)}
.about-photo{left:632px;top:1474px;width:410px;height:410px;border-radius:50%;background:radial-gradient(circle at 55% 40%,#e9e2d8 0%,#b9a898 45%,#6f6a70 80%,#4b4a55 100%)}

/* products */
.products-band{left:0;top:1985px;width:1200px;height:417px;background:linear-gradient(90deg,#f3bc00 0%,#fcc200 40%,#e9b400 70%,#f6c000 100%)}
.products-title{top:2065px;font-size:42px;font-weight:700}
.products-bar{left:555px;top:2126px;width:90px;height:9px;background:var(--ink)}
.card{position:absolute;top:2174px;width:427px;height:370px;background:var(--white);box-shadow:0 6px 18px rgba(0,0,0,.08)}
.card-img{position:absolute;left:60px;top:30px;width:307px;height:230px;background:linear-gradient(135deg,#f4f4f4 0%,#e3e3e3 55%,#cfd2d2 100%)}
.card-name{position:absolute;left:0;top:290px;width:427px;text-align:center;font-size:20px;font-weight:500;line-height:26px;color:var(--ink)}

/* carriers */
.carriers-title{top:2630px;font-size:15px;font-weight:500}
.carriers{left:236px;top:2679px;width:728px;height:78px;display:flex;border:1px solid #e3e3e3}
.carrier{flex:1;display:flex;align-items:center;justify-content:center;gap:8px;border-right:1px solid #e3e3e3;font-size:20px;font-weight:500;color:var(--text)}
.carrier:last-child{border-right:0}
.carrier i{width:12px;height:12px;border-radius:50%;background:var(--yellow);display:block}

/* contact */
.contact-title{top:2858px;font-size:33px}
.contact-text{left:0;top:2916px;width:1200px;text-align:center;font-size:13.5px;line-height:22px;color:var(--muted)}
.field{position:absolute;border:1px solid #bdbdbd;background:var(--white);font-size:12px;color:var(--muted);padding:10px 11px}

/* footer */
.footer-cut{left:0;top:3236px}
.footer{left:0;top:3400px;width:1200px;height:350px;background:var(--ink)}
.foot-brand{left:165px;top:3522px;font-size:34px;font-weight:500;color:var(--white)}
.foot-mark{left:230px;top:3468px;width:36px;height:36px;background:var(--yellow)}
.foot-tag{left:165px;top:3565px;font-size:14px;font-weight:500;color:var(--yellow)}
.foot-head{top:3441px;font-size:15px;font-weight:500;color:var(--white);text-transform:uppercase}
.foot-rule{top:3482px;width:138px;height:2px;background:var(--white)}
.foot-rule::before{content:"";position:absolute;left:0;top:-3px;width:8px;height:8px;background:var(--yellow)}
.foot-link{font-size:14px;color:var(--white)}
.foot-ico{width:26px;height:26px;border-radius:50%;background:var(--yellow)}
.foot-dot{width:14px;height:14px;background:var(--yellow)}
.foot-divider{left:146px;top:3672px;width:897px;height:1px;background:#444}
.copyright{left:0;top:3702px;width:1200px;text-align:center;font-size:12px;color:var(--white)}
</style>
</head>
<body>
<div class="page">

  <!-- header -->
  <div class="abs topline"></div>
  <header class="abs header"></header>
  <div class="abs brand"><span class="brand-mark"></span><span class="brand-name">Nestor Bolt</span></div>
  <div class="abs brand-tag">MOBILE SIGNAL BOOSTER</div>
  <div class="abs question">
    <svg width="15" height="15" viewBox="0 0 24 24"><path fill="#111" d="M6.6 10.8a15.1 15.1 0 0 0 6.6 6.6l2.2-2.2c.3-.3.7-.4 1-.2 1.1.4 2.3.6 3.6.6.6 0 1 .4 1 1V20c0 .6-.4 1-1 1A17 17 0 0 1 3 4c0-.6.4-1 1-1h3.5c.6 0 1 .4 1 1 0 1.3.2 2.5.6 3.6.1.3 0 .7-.2 1z"/></svg>
    <span>Have a question?: <b>123 555 0187</b></span>
  </div>
  <nav>
    <div class="abs nav active" style="left:473px">Home</div>
    <div class="abs nav" style="left:572px">Solutions / How it works</div>
    <div class="abs nav" style="left:827px">Case Studies</div>
    <div class="abs nav" style="left:984px">Contact</div>
  </nav>

  <!-- hero -->
  <div class="abs hero-photo" role="img" aria-label="Woman relaxing on a sofa at home, smiling at her mobile phone"></div>
  <div class="abs hero-kicker">Nestor Bolt</div>
  <h1 class="abs hero-title">Mobile Signal<br>Booster Solutions</h1>
  <div class="btn" style="left:150px;top:409px;width:146px;height:45px">Order Now</div>
  <svg class="abs hero-cut" width="1200" height="100" viewBox="0 0 1200 100">
    <polygon points="0,90 560,56 1200,20 1200,100 0,100" fill="#ffffff"/>
    <polygon points="560,56 1200,8 1200,90" fill="#fcc200"/>
  </svg>

  <!-- how it works -->
  <h2 class="section-title" style="top:866px;font-size:32px">How Signal Booster Work ?</h2>
  <svg class="abs steps" width="1200" height="220" viewBox="0 940 1200 220">
    <path d="M68 1105 C200 1040 230 1020 277 1019 C380 1017 420 1045 492 1038 C560 1032 640 1060 703 1048 C780 1035 830 1000 914 1005 C1000 1010 1060 1060 1120 1135" fill="none" stroke="#111" stroke-width="2"/>
    <g fill="#fff" stroke="#111" stroke-width="2">
      <circle cx="179" cy="1051" r="54"/><circle cx="390" cy="1008" r="54"/><circle cx="601" cy="1051" r="54"/><circle cx="812" cy="1008" r="54"/><circle cx="1024" cy="1051" r="54"/>
    </g>
    <g fill="#fcc200">
      <circle cx="179" cy="1051" r="48"/><circle cx="390" cy="1008" r="48"/><circle cx="601" cy="1051" r="48"/><circle cx="812" cy="1008" r="48"/><circle cx="1024" cy="1051" r="48"/>
    </g>
    <g fill="none" stroke="#111" stroke-width="2.5" stroke-linecap="round" stroke-linejoin="round">
      <path d="M179 1045 L168 1075 M179 1045 L190 1075 M172 1064 H186"/><circle cx="179" cy="1042" r="3"/>
      <path d="M166 1032 a18 18 0 0 0 0 20 M192 1032 a18 18 0 0 1 0 20"/>
      <path d="M378 985 V1030 M402 985 V1030 M378 985 a12 12 0 0 1 24 0"/>
      <rect x="588" y="1033" width="26" height="36" rx="4"/><rect x="597" y="1046" width="8" height="11"/>
      <rect x="799" y="985" width="18" height="28" rx="2"/><path d="M817 995 h8 M817 1003 h8 M808 1013 v16"/>
      <path d="M1003 1038 l8 22 M1045 1038 l-8 22"/><rect x="1003" y="1060" width="42" height="12" rx="2"/><path d="M1014 1046 a14 14 0 0 1 20 0 M1019 1051 a7 7 0 0 1 10 0"/>
    </g>
    <g>
      <circle cx="277" cy="1019" r="10" fill="#111"/><circle cx="492" cy="1038" r="10" fill="#111"/><circle cx="703" cy="1048" r="10" fill="#111"/><circle cx="914" cy="1005" r="10" fill="#111"/>
      <g fill="none" stroke="#fff" stroke-width="2"><path d="M275 1015 l4 4 l-4 4"/><path d="M490 1034 l4 4 l-4 4"/><path d="M701 1044 l4 4 l-4 4"/><path d="M912 1001 l4 4 l-4 4"/></g>
    </g>
  </svg>
  <p class="step-caption" style="left:94px;top:1131px">The outdoor antenna captures signal from the signal tower.</p>
  <p class="step-caption" style="left:305px;top:1087px">The outdoor antenna transfers the signal to the cell booster via the coaxial cable.</p>
  <p class="step-caption" style="left:516px;top:1131px">The booster amplifies cell signal and sends it to the indoor antenna.</p>
  <p class="step-caption" style="left:727px;top:1087px">The indoor antenna rebroadcasts the signal insides to all mobile devices.</p>
  <p class="step-caption" style="left:939px;top:1131px">The booster amplifies outgoing cell signal back to the signal tower.</p>
  <div class="btn" style="left:527px;top:1235px;width:146px;height:44px">Order Now</div>

  <!-- about -->
  <section class="abs about"></section>
  <h2 class="abs about-title">About the Company</h2>
  <p class="abs about-sub">Lorem ipsum dolor sit ametconse<br>ctetur adipiscing elitsed do</p>
  <p class="abs about-text">Lorem ipsum dolor sit amet, consectetur adipiscing elit, sed do eiusmod tempor incididunt ut labore et dolore magna aliquauis ipsum suspendisse ultrices gravida. Risus commodo viverra maecenas accumsan lacus vel facilisis. Lorem ipsum dolorsit amet, consectetur adipiscing elit, sed do eiusmod temploreor incididunt ut labore et dolore magna aliqua.</p>
  <div class="btn" style="left:150px;top:1792px;width:144px;height:45px">Read More</div>
  <div class="abs about-ring"></div>
  <div class="abs about-photo" role="img" aria-label="Family sitting together on a sofa looking at a mobile phone"></div>

  <!-- products -->
  <div class="abs products-band" role="img" aria-label="Yellow tinted photo of people using phones at home"></div>
  <h2 class="section-title products-title">Our Products</h2>
  <div class="abs products-bar"></div>
  <article class="card" style="left:157px">
    <div class="card-img" role="img" aria-label="Signal booster unit with antennas and coaxial cables"></div>
    <h3 class="card-name">Lorem ipsum dolor sit amet<br>consectetur adipiscing</h3>
  </article>
  <article class="card" style="left:607px">
    <div class="card-img" role="img" aria-label="Signal booster unit with antennas and coaxial cables"></div>
    <h3 class="card-name">Lorem ipsum dolor sit amet<br>consectetur adipiscing</h3>
  </article>

  <h3 class="section-title carriers-title">Works for 2G, 3G, and 4G LTE networks on all carriers</h3>
  <div class="abs carriers">
    <div class="carrier"><i></i>Kuvo</div>
    <div class="carrier"><i></i>Veltaro</div>
    <div class="carrier"><i></i>Aerlink</div>
    <div class="carrier"><i></i>Ixora</div>
    <div class="carrier"><i></i>Brintel</div>
  </div>

  <!-- contact -->
  <h2 class="section-title contact-title">Contact Us</h2>
  <p class="contact-text">Lorem ipsum dolor sit amet, consectetur adipiscing elit, sed do eiusmod tempor incididunt ut<br>labore et dolore magna aliquauis ipsum suspendisse ultrices gravidaus commod</p>
  <div class="field" style="left:278px;top:2996px;width:210px;height:38px">Name</div>
  <div class="field" style="left:496px;top:2996px;width:210px;height:38px">Email</div>
  <div class="field" style="left:712px;top:2996px;width:210px;height:38px">Phone</div>
  <div class="field" style="left:278px;top:3043px;width:644px;height:144px">Message</div>
  <div class="btn" style="left:533px;top:3164px;width:134px;height:47px;font-size:15px">Submit Now</div>

  <!-- footer -->
  <svg class="abs footer-cut" width="1200" height="170" viewBox="0 0 1200 170">
    <defs>
      <linearGradient id="footGlow" x1="0" x2="1" y1="0" y2="0">
        <stop offset="0" stop-color="#fcc200" stop-opacity="0"/>
        <stop offset=".55" stop-color="#fcc200" stop-opacity=".15"/>
        <stop offset="1" stop-color="#fcc200" stop-opacity=".9"/>
      </linearGradient>
    </defs>
    <polygon points="0,0 320,52 0,40" fill="#fcc200"/>
    <polygon points="500,40 1200,30 1200,150 900,110" fill="url(#footGlow)"/>
    <polygon points="0,30 1200,150 1200,170 0,170" fill="#111"/>
  </svg>
  <footer class="abs footer"></footer>
  <div class="abs foot-mark"></div>
  <div class="abs foot-brand">Nestor Bolt</div>
  <div class="abs foot-tag">MOBILE SIGNAL BOOSTER</div>

  <div class="abs foot-head" style="left:392px">Quick Links</div>
  <div class="abs foot-rule" style="left:392px"></div>
  <div class="abs foot-link" style="left:399px;top:3515px">Home</div>
  <div class="abs foot-link" style="left:399px;top:3539px">Solutions / How it works</div>
  <div class="abs foot-link" style="left:399px;top:3563px">Case Studies</div>
  <div class="abs foot-link" style="left:399px;top:3587px">Contact</div>

  <div class="abs foot-head" style="left:604px">Contact</div>
  <div class="abs foot-rule" style="left:604px"></div>
  <div class="abs foot-ico" style="left:604px;top:3511px"></div>
  <svg class="abs" style="left:610px;top:3519px" width="14" height="10" viewBox="0 0 14 10"><rect x=".5" y=".5" width="13" height="9" fill="#fff"/><path d="M.5 .5 L7 6 L13.5 .5" fill="none" stroke="#fcc200"/></svg>
  <div class="abs foot-link" style="left:644px;top:3514px">info@nestorbolt.com</div>
  <div class="abs foot-ico" style="left:604px;top:3557px"></div>
  <svg class="abs" style="left:610px;top:3563px" width="14" height="14" viewBox="0 0 24 24"><path fill="#fff" d="M6.6 10.8a15.1 15.1 0 0 0 6.6 6.6l2.2-2.2c.3-.3.7-.4 1-.2 1.1.4 2.3.6 3.6.6.6 0 1 .4 1 1V20c0 .6-.4 1-1 1A17 17 0 0 1 3 4c0-.6.4-1 1-1h3.5c.6 0 1 .4 1 1 0 1.3.2 2.5.6 3.6.1.3 0 .7-.2 1z"/></svg>
  <div class="abs foot-link" style="left:644px;top:3561px">PH:(212) 555-0143</div>

  <div class="abs foot-head" style="left:882px">Follow Me</div>
  <div class="abs foot-rule" style="left:882px"></div>
  <div class="abs foot-dot" style="left:888px;top:3518px"></div>
  <div class="abs foot-link" style="left:920px;top:3515px">Friendwall</div>
  <div class="abs foot-dot" style="left:888px;top:3565px"></div>
  <div class="abs foot-link" style="left:920px;top:3562px">Chirper</div>
  <div class="abs foot-dot" style="left:888px;top:3612px"></div>
  <div class="abs foot-link" style="left:920px;top:3610px">Linkhall</div>

  <div class="abs foot-divider"></div>
  <div class="abs copyright">Copyright © 2023 Nestor Bolt. All rights Reserved</div>
</div>
</body>
</html>
```